Business Card Design Project

I need a business card design for an Organic drive thru coffee kiosk. We will serve organic coffee, teas & smoothies and will serve healthy breakfast food/snacks for people on the go.
I want the card to have 2-3 colors max (earthy colors like browns, greens and so on).
I have attached the logo I want used and would love to play off the theme of "balance."
Include:
Tidy-Kettle Coffee
address: 4820 Gorvin Ct. Raleigh, NC 27583
phone: 919-731-4062
website: www.tidy-kettle.com (website is not up yet but still include it on card)
email: Rosalind@tidy-kettle.com
I want one of the following sayings somewhere on the card (the front or back is fine):
"Eat & Drink Well, on the run!"
"Break the fast with Tidy-Kettle"
Maybe on the back list what we offer:
-Organic coffee, espresso & tea
-Blendora smoothies & protein shakes
-Zesty Pour (100% fresh local fruit and veggies)
-Tender Nibs

```html
<!DOCTYPE html>
<html lang="en">
<head>
<meta charset="utf-8">
<title>Tidy-Kettle Coffee — Business Card</title>
<link rel="stylesheet" href="https://fonts.googleapis.com/css2?family=Ubuntu:wght@400;500;700&family=Italianno&family=Cormorant+Garamond:ital,wght@1,500&display=swap">
<style>
  :root {
    --page: #e8e5e0;
    --espresso: #140806;
    --roast: #2a0e09;
    --ember: #8e1d12;
    --ring: #7d2617;
    --bean: #4a2619;
    --cream: #ffffff;
    --gold: #e9c98b;
    --latte: #dccab3;
  }
  * { box-sizing: border-box; margin: 0; padding: 0; }
  html, body {
    width: 1200px; height: 787px; overflow: hidden;
    background: var(--page);
  }
  .sheet {
    position: relative; width: 1200px; height: 787px;
    display: flex; align-items: center; justify-content: center; gap: 40px;
  }
  .card {
    position: relative; width: 560px; height: 320px; overflow: hidden;
    box-shadow: 0 6px 18px rgba(0,0,0,.25);
    font-family: "Ubuntu", sans-serif;
  }
  .card-bg { position: absolute; inset: 0; width: 100%; height: 100%; }

  /* Front */
  .brand-mark {
    position: absolute; left: 40px; top: 30px; width: 170px;
    display: flex; flex-direction: column; align-items: center;
  }
  .brand-dot {
    width: 34px; height: 34px; border-radius: 50%; background: var(--bean);
    margin-bottom: 8px;
  }
  .brand-name {
    font-size: 28px; font-weight: 500; color: var(--bean); letter-spacing: .5px;
  }
  .brand-tagline {
    margin-top: 4px; font-size: 8.5px; font-weight: 700; letter-spacing: 1.6px;
    color: var(--ember);
  }
  .cup-art {
    position: absolute; left: 60px; top: 178px; width: 170px; height: 130px;
    border-radius: 40% 40% 46% 46%;
    background: radial-gradient(ellipse at 55% 40%, #ffffff 0%, #e7e5e3 55%, #cfcac6 100%);
  }
  .front-info {
    position: absolute; right: 30px; top: 88px; text-align: right;
  }
  .front-title {
    font-size: 38px; font-weight: 500; color: var(--cream); line-height: 1;
  }
  .front-script {
    font-family: "Italianno", cursive; font-size: 40px; color: var(--cream);
    line-height: .9; margin-top: 2px;
  }
  .contact {
    list-style: none; margin-top: 22px; color: var(--gold);
    font-size: 14.5px; line-height: 1.32;
  }
  .contact .address { margin-right: 0; }

  /* Back */
  .back-cup {
    position: absolute; left: 26px; top: 150px; width: 130px; height: 96px;
    border-radius: 40% 40% 46% 46%;
    background: radial-gradient(ellipse at 55% 40%, #ffffff 0%, #e6e3e0 55%, #cbc5c0 100%);
  }
  .back-brand {
    position: absolute; left: 70px; top: 262px;
    display: flex; align-items: center; gap: 6px;
  }
  .back-brand .brand-dot { width: 22px; height: 22px; margin: 0; }
  .back-brand .brand-name { font-size: 20px; }
  .offer {
    position: absolute; right: 28px; top: 22px; text-align: right;
  }
  .offer-heading {
    font-size: 13.5px; font-weight: 700; color: var(--cream); margin-bottom: 14px;
  }
  .offer-list {
    list-style: none; color: var(--latte); font-size: 12.5px; line-height: 2.15;
  }
  .slogan {
    position: absolute; right: 28px; top: 236px; text-align: right;
  }
  .slogan-quote {
    font-family: "Cormorant Garamond", serif; font-style: italic; font-weight: 500;
    font-size: 21px; color: var(--cream);
  }
  .slogan-web {
    margin-top: 2px; font-size: 12px; letter-spacing: 6px; color: var(--latte);
  }
</style>
</head>
<body>
<main class="sheet">

  <section class="card card-front" aria-label="Business card front">
    <svg class="card-bg" viewBox="0 0 560 320" aria-hidden="true">
      <defs>
        <radialGradient id="front-glow" cx="0.5" cy="0.05" r="0.75">
          <stop offset="0" stop-color="var(--ember)"/>
          <stop offset="0.45" stop-color="var(--roast)"/>
          <stop offset="1" stop-color="var(--espresso)"/>
        </radialGradient>
      </defs>
      <rect width="560" height="320" fill="url(#front-glow)"/>
      <path d="M0,0 H278 C310,95 300,225 222,320 H0 Z" fill="var(--ring)"/>
      <path d="M0,0 H270 C301,95 291,225 213,320 H0 Z" fill="var(--cream)"/>
    </svg>

    <div class="brand-mark">
      <span class="brand-dot"></span>
      <span class="brand-name">Tidy-Kettle</span>
      <span class="brand-tagline">ORGANIC COFFEE + CAFE</span>
    </div>

    <div class="cup-art" role="img" aria-label="Steaming white cup of black coffee on a saucer with roasted coffee beans beside it"></div>

    <div class="front-info">
      <h1 class="front-title">Tidy-Kettle</h1>
      <p class="front-script">Coffee</p>
      <ul class="contact">
        <li class="address">4820 Gorvin Ct. Raleigh, NC 27583</li>
        <li>919-731-4062</li>
        <li>www.tidy-kettle.com</li>
        <li>Rosalind@tidy-kettle.com</li>
      </ul>
    </div>
  </section>

  <section class="card card-back" aria-label="Business card back">
    <svg class="card-bg" viewBox="0 0 560 320" aria-hidden="true">
      <defs>
        <radialGradient id="back-glow" cx="0.4" cy="0.5" r="0.7">
          <stop offset="0" stop-color="var(--ember)"/>
          <stop offset="0.45" stop-color="var(--roast)"/>
          <stop offset="1" stop-color="var(--espresso)"/>
        </radialGradient>
      </defs>
      <rect width="560" height="320" fill="url(#back-glow)"/>
      <circle cx="100" cy="262" r="158" fill="var(--ring)"/>
      <circle cx="100" cy="262" r="152" fill="var(--cream)"/>
    </svg>

    <div class="back-cup" role="img" aria-label="Steaming white cup of black coffee with a few roasted coffee beans"></div>

    <div class="back-brand">
      <span class="brand-dot"></span>
      <span class="brand-name">Tidy-Kettle</span>
    </div>

    <div class="offer">
      <h2 class="offer-heading">We offer:</h2>
      <ul class="offer-list">
        <li>-Organic coffee, espresso &amp; tea</li>
        <li>-Blendora smoothies &amp; protein shakes</li>
        <li>-Zesty Pour (100% fresh local fruit and veggies)</li>
        <li>-Tender Nibs</li>
      </ul>
    </div>

    <div class="slogan">
      <p class="slogan-quote">“Break the fast with Tidy-Kettle”</p>
      <p class="slogan-web">www.tidy-kettle.com</p>
    </div>
  </section>

</main>
</body>
</html>
```